Home Care company needs letter head branding

Home care company needs a letter head which can be used for all documents the company's clients view. We provided in home care for the elderly. We would like to use our company colors (2785A7, 0A4057 and 34A74D) and should not be too large as we will be using it on more than just a letter head but all documents our clients sign / receive.
Target Market(s)
Professional business
Industry/Entity Type
Health Care
Requirements
Must have
- corporate brand colors

```html
<!DOCTYPE html>
<html lang="en">
<head>
<meta charset="utf-8">
<title>Elmhaven Care – Letterhead</title>
<link href="https://fonts.googleapis.com/css2?family=Lato:wght@400;700&family=Roboto:wght@500&family=Great+Vibes&display=swap" rel="stylesheet">
<style>
  :root {
    --brand-blue: #2785A7;
    --brand-ink: #3a3a3c;
    --brand-dark: #0A4057;
    --paper: #f6f6f6;
    --backdrop: #c2c2c2;
    --text: #2b2b2b;
  }
  * { box-sizing: border-box; margin: 0; padding: 0; }
  html, body { width: 1200px; height: 1200px; overflow: hidden; }
  body { background: var(--backdrop); position: relative; font-family: "Lato", sans-serif; color: var(--text); }

  .letterhead {
    position: absolute; left: 170px; top: 44px;
    width: 836px; height: 1080px;
    background: var(--paper);
    transform: scale(1.03); transform-origin: top left;
    box-shadow: 0 6px 18px rgba(0,0,0,.18);
  }
  .letterhead-frame { position: absolute; inset: 0; }

  .brand { position: absolute; left: 533px; top: 22px; display: flex; align-items: center; gap: 12px; }
  .brand-dot { width: 58px; height: 58px; border-radius: 50%; background: var(--brand-blue); }
  .brand-name { font-family: "Lato", sans-serif; font-weight: 700; font-size: 31px; color: var(--brand-blue); white-space: nowrap; }

  .recipient { position: absolute; left: 102px; top: 182px; }
  .recipient-label { font-size: 13px; }
  .recipient-name { font-size: 24px; letter-spacing: .3px; margin-top: 6px; line-height: 1; }
  .recipient-role { font-size: 13px; margin-top: 3px; }

  .letter-body { position: absolute; left: 108px; top: 288px; width: 666px; }
  .letter-body p { font-size: 12.6px; line-height: 19.3px; text-align: justify; margin-bottom: 8.5px; }

  .sign-off { position: absolute; left: 110px; top: 704px; width: 90px; }
  .sign-off-word { font-size: 12.5px; text-align: right; }
  .signature { font-family: "Great Vibes", cursive; font-size: 28px; line-height: 1; margin-top: 2px; }
  .signer-role { font-size: 12px; position: absolute; right: -2px; top: 44px; }

  .contact { position: absolute; right: 0; top: 932px; display: flex; }
  .contact-values { text-align: right; font-family: "Roboto", sans-serif; font-weight: 500; font-size: 13.5px; padding-right: 10px; padding-top: 12px; }
  .contact-values div { height: 25.5px; }
  .contact-keys { width: 41px; height: 102px; background: var(--brand-blue); color: #fff; font-family: "Roboto", sans-serif; font-weight: 500; font-size: 13px; padding: 12px 0 0 10px; }
  .contact-keys div { height: 25.5px; }
</style>
</head>
<body>
  <main class="letterhead">
    <svg class="letterhead-frame" viewBox="0 0 836 1080" width="836" height="1080" aria-hidden="true">
      <path fill="var(--brand-blue)" d="M0 0 H522 C522 38 498 62 456 62 H84 Q41 62 41 104 V832 L0 850 Z"/>
      <path fill="var(--brand-ink)" d="M0 862 L41 844 V1080 H0 Z"/>
    </svg>

    <div class="brand">
      <span class="brand-dot"></span>
      <span class="brand-name">Elmhaven Care</span>
    </div>

    <section class="recipient">
      <p class="recipient-label">To,</p>
      <p class="recipient-name">JOHNDOE</p>
      <p class="recipient-role">DESIGNER</p>
    </section>

    <section class="letter-body">
      <p>Lorem Ipsum is simply dummy text of the printing and typesetting industry. Lorem Ipsum has been the industry's standard dummy text ever since the 1500s, when an unknown printer took a galley of type and scrambled it to make a type specimen book. It has survived not only five centuries, but also the leap into electronic typesetting, remaining essentially unchanged. It was popularised in the 1960s with the release of Letraset sheets containing Lorem Ipsum passages, and more recently with desktop publishing software like Aldus PageMaker including versions of Lorem Ipsum.</p>
      <p>Lorem Ipsum is simply dummy text of the printing and typesetting industry. Lorem Ipsum has been the industry's standard dummy text ever since the 1500s, when an unknown printer took a galley of type and scrambled it to make a type specimen book. It has survived not only five centuries, but also the leap into electronic typesetting, remaining essentially unchanged. It was popularised in the 1960s with the release of Letraset sheets containing Lorem Ipsum passages, and more recently with desktop publishing software like Aldus PageMaker including versions of Lorem Ipsum.</p>
      <p>Lorem Ipsum is simply dummy text of the printing and typesetting industry. Lorem Ipsum has been the industry's standard dummy text ever since the 1500s, when an unknown printer took a galley of type and scrambled it to make a type specimen book. It has survived not only five centuries, but also the leap into electronic typesetting, remaining essentially unchanged. It was popularised in the 1960s with the release of Letraset sheets containing Lorem Ipsum passages, and more recently with desktop publishing software like Aldus PageMaker including versions of Lorem Ipsum.</p>
    </section>

    <section class="sign-off">
      <p class="sign-off-word">Sincerely,</p>
      <p class="signature">Johndoe</p>
      <p class="signer-role">Manager</p>
    </section>

    <footer class="contact">
      <div class="contact-values">
        <div>+ 0 123 456 789</div>
        <div>lorem@ipsum.com</div>
        <div>websitename.com</div>
      </div>
      <div class="contact-keys">
        <div>P.</div>
        <div>M.</div>
        <div>W.</div>
      </div>
    </footer>
  </main>
</body>
</html>
```